Stationery Design for a fast food resturaunt

We just created our logo, we need nice stationary to go with it. We beed the design to be on white background and black background.

Target Market(s)

Landlords who will lease their retail shops to us. Shopping Mall Management.Real Estate Professionals.

Font styles to use
Sans Serif

```html
<!DOCTYPE html>
<html lang="en">
<head>
<meta charset="utf-8">
<title>Amber Crest – Letterhead</title>
<link href="https://fonts.googleapis.com/css2?family=Montserrat:wght@300;700&family=Arimo:wght@400&display=swap" rel="stylesheet">
<style>
  :root {
    --amber: #fdb913;
    --paper-white: #ffffff;
    --paper-black: #000000;
    --ink: #000000;
    --charcoal: #3d3d3d;
    --watermark-light: #e6e7e8;
    --watermark-dark: #1e1e1e;
  }
  html, body {
    margin: 0;
    padding: 0;
    width: 1200px;
    height: 1000px;
    overflow: hidden;
    background: var(--amber);
  }
  .canvas {
    position: relative;
    width: 1200px;
    height: 1000px;
  }
  .letterhead {
    position: absolute;
    top: 173px;
    width: 493px;
    height: 687px;
    overflow: hidden;
  }
  .letterhead--light { left: 107px; background: var(--paper-white); }
  .letterhead--dark  { left: 675px; background: var(--paper-black); }

  .brand-block {
    position: absolute;
    left: 26px;
    top: 0;
    width: 109px;
    height: 85px;
    display: flex;
    flex-direction: column;
    align-items: center;
    justify-content: center;
  }
  .letterhead--light .brand-block { background: var(--ink); }
  .letterhead--dark  .brand-block { background: var(--charcoal); }
  .brand-name {
    font-family: "Montserrat", sans-serif;
    font-weight: 300;
    font-size: 15px;
    line-height: 17px;
    letter-spacing: 0.5px;
    color: var(--amber);
    text-align: center;
    margin: 0;
  }
  .brand-rule {
    position: absolute;
    left: 26px;
    top: 89px;
    width: 109px;
    height: 4px;
    background: var(--amber);
  }

  .watermark {
    position: absolute;
    left: -6px;
    top: 250px;
    width: 520px;
    font-family: "Montserrat", sans-serif;
    font-weight: 700;
    font-size: 150px;
    line-height: 180px;
    letter-spacing: 4px;
    white-space: nowrap;
    margin: 0;
  }
  .letterhead--light .watermark { color: var(--watermark-light); }
  .letterhead--dark  .watermark { color: var(--watermark-dark); }

  .footer-rule {
    position: absolute;
    left: 26px;
    top: 650px;
    width: 442px;
    height: 2px;
    background: var(--amber);
  }
  .contact-line {
    position: absolute;
    left: 27px;
    top: 658px;
    width: 442px;
    font-family: "Arimo", sans-serif;
    font-size: 7.4px;
    letter-spacing: 0.35px;
    white-space: nowrap;
    margin: 0;
  }
  .letterhead--light .contact-line { color: var(--ink); }
  .letterhead--dark  .contact-line { color: var(--paper-white); }
  .contact-line .sep,
  .contact-line .label { color: var(--amber); }
  .footer-band {
    position: absolute;
    left: 26px;
    top: 672px;
    width: 442px;
    height: 15px;
  }
  .letterhead--light .footer-band { background: var(--ink); }
  .letterhead--dark  .footer-band { background: var(--charcoal); }
</style>
</head>
<body>
<main class="canvas">

  <section class="letterhead letterhead--light" aria-label="Letterhead on white">
    <div class="brand-block"><p class="brand-name">AMBER<br>CREST</p></div>
    <div class="brand-rule"></div>
    <p class="watermark" aria-hidden="true">AMBER</p>
    <div class="footer-rule"></div>
    <p class="contact-line">Address line 1, City 555555 <span class="sep">|</span> <span class="label">(T)</span> +1 999.999.9999 <span class="sep">|</span> <span class="label">(F)</span> + 1 888.888.8888 <span class="sep">|</span> enquiry@website.com <span class="sep">|</span> www.website.com</p>
    <div class="footer-band"></div>
  </section>

  <section class="letterhead letterhead--dark" aria-label="Letterhead on black">
    <div class="brand-block"><p class="brand-name">AMBER<br>CREST</p></div>
    <div class="brand-rule"></div>
    <p class="watermark" aria-hidden="true">AMBER</p>
    <div class="footer-rule"></div>
    <p class="contact-line">Address line 1, City 555555 <span class="sep">|</span> <span class="label">(T)</span> +1 999.999.9999 <span class="sep">|</span> <span class="label">(F)</span> + 1 888.888.8888 <span class="sep">|</span> enquiry@website.com <span class="sep">|</span> www.website.com</p>
    <div class="footer-band"></div>
  </section>

</main>
</body>
</html>
```